New business card for civil engineering company - "Keystone Audit"

We need a business card designed for our new structural engineering company.

The company name is "Keystone Audit" logo files attached.

We would like the following:
* Two-sided card
* Simple design

Information to be placed on the card:
Name - Marcus Dellow
Job Title - Director / Structural Engineer
Credentials - BEng(Hons), CPEng, CMengNZ, IntPE(NZ)
Email - marcus.dellow@keystoneaudit.co.nz
mobile - 0219364058
website - www.keystoneaudit.co.nz

```html
<!DOCTYPE html>
<html lang="en">
<head>
<meta charset="utf-8">
<title>Keystone Audit — Business Card</title>
<link rel="stylesheet" href="https://fonts.googleapis.com/css2?family=Open+Sans:wght@400;600;700&display=swap">
<style>
  :root {
    --page: #ffffff;
    --ink-black: #0b0c0e;
    --back-black: #000000;
    --navy: #001d5e;
    --blue: #185494;
    --white: #ffffff;
    --icon-grey: #6b6b6b;
    --mark-grey: #8a8a8a;
  }
  html, body {
    margin: 0;
    width: 1200px;
    height: 1200px;
    overflow: hidden;
    background: var(--page);
  }
  .sheet {
    position: relative;
    width: 1200px;
    height: 1200px;
  }
  .card {
    position: absolute;
    left: 293px;
    width: 639px;
    height: 355px;
    display: block;
  }
  .card--front { top: 235px; }
  .card--back { top: 653px; }
  .card text {
    font-family: "Open Sans", Arial, sans-serif;
    fill: var(--white);
  }
  .brand-name { font-weight: 600; letter-spacing: 4px; }
  .web-label { font-size: 20px; }
  .contact-text { font-size: 20px; }
  .person-name { font-size: 36px; font-weight: 400; }
  .person-name .surname { font-weight: 700; }
  .person-role { font-size: 20px; }
  .icon-disc { fill: var(--icon-grey); }
  .icon-glyph { fill: var(--white); }
  .icon-stroke { fill: none; stroke: var(--white); stroke-width: 1.6; }
</style>
</head>
<body>
<main class="sheet">

  <!-- Front side -->
  <svg class="card card--front" viewBox="0 0 1029 571" aria-label="Keystone Audit business card, front">
    <defs>
      <linearGradient id="front-band-tone" x1="0" y1="0" x2="0" y2="1">
        <stop offset="0" stop-color="var(--blue)"/>
        <stop offset="1" stop-color="var(--navy)"/>
      </linearGradient>
    </defs>
    <rect width="1029" height="571" fill="var(--ink-black)"/>
    <rect class="accent-band" role="img" aria-label="Angular blue decorative band" x="0" y="360" width="1029" height="211" fill="url(#front-band-tone)"/>

    <rect class="brand-mark" x="481" y="150" width="68" height="68" fill="var(--mark-grey)"/>
    <text class="brand-name" x="515" y="305" font-size="38" text-anchor="middle">KEYSTONE AUDIT</text>

    <g class="web-icon" transform="translate(732,523)">
      <circle r="12" class="icon-glyph"/>
      <path d="M-10,-3 L10,3 M-4,-11 L3,11 M-10,5 L6,-9" stroke="var(--navy)" stroke-width="1.6"/>
    </g>
    <text class="web-label" x="752" y="530">www.keystoneaudit.co.nz</text>
  </svg>

  <!-- Back side -->
  <svg class="card card--back" viewBox="0 0 1029 571" aria-label="Keystone Audit business card, back">
    <defs>
      <linearGradient id="back-panel-tone" x1="0" y1="0" x2="1" y2="0">
        <stop offset="0" stop-color="var(--blue)"/>
        <stop offset="0.45" stop-color="var(--navy)"/>
      </linearGradient>
      <linearGradient id="back-strip-tone" x1="0" y1="0" x2="1" y2="0">
        <stop offset="0" stop-color="var(--blue)"/>
        <stop offset="1" stop-color="var(--back-black)"/>
      </linearGradient>
    </defs>
    <rect width="1029" height="571" fill="var(--back-black)"/>
    <rect class="accent-panel" role="img" aria-label="Angular blue decorative panel" x="610" y="0" width="419" height="571" fill="url(#back-panel-tone)"/>
    <rect class="accent-strip" role="img" aria-label="Angular blue decorative strip" x="0" y="530" width="490" height="41" fill="url(#back-strip-tone)"/>

    <rect class="brand-mark" x="96" y="64" width="54" height="54" fill="var(--mark-grey)"/>
    <text class="brand-name" x="170" y="106" font-size="34">KEYSTONE AUDIT</text>
    <line class="divider" x1="56" y1="175" x2="529" y2="175" stroke="var(--white)" stroke-width="2"/>

    <g class="contact contact--credentials">
      <circle class="icon-disc" cx="73" cy="226" r="23"/>
      <path class="icon-glyph" d="M60,228 L73,215 L86,228 L82,228 L82,239 L76,239 L76,232 L70,232 L70,239 L64,239 L64,228 Z"/>
      <text class="contact-text" x="102" y="233">BEng(Hons), CPEng, CMengNZ, IntPE(NZ)</text>
    </g>
    <g class="contact contact--email">
      <circle class="icon-disc" cx="73" cy="295" r="23"/>
      <path class="icon-glyph" d="M60,285 L88,297 L72,299 L68,308 Z"/>
      <text class="contact-text" x="104" y="302">marcus.dellow@keystoneaudit.co.nz</text>
    </g>
    <g class="contact contact--phone">
      <circle class="icon-disc" cx="73" cy="366" r="23"/>
      <path class="icon-glyph" d="M60,362 Q73,352 86,362 L86,366 L80,366 L80,363 L66,363 L66,366 L60,366 Z M63,368 L83,368 L83,377 L63,377 Z"/>
      <circle cx="73" cy="372" r="3" fill="var(--icon-grey)"/>
      <text class="contact-text" x="102" y="373">0219364058</text>
    </g>
    <g class="contact contact--web">
      <circle class="icon-disc" cx="73" cy="438" r="23"/>
      <circle class="icon-stroke" cx="73" cy="438" r="11"/>
      <path class="icon-stroke" d="M63,435 L83,441 M69,427 L76,449 M63,443 L79,429"/>
      <text class="contact-text" x="104" y="445">www.keystoneaudit.co.nz</text>
    </g>

    <text class="person-name" x="837" y="258" text-anchor="middle">MARCUS <tspan class="surname">DELLOW</tspan></text>
    <text class="person-role" x="837" y="286" text-anchor="middle">Director / Structural Engineer</text>
  </svg>

</main>
</body>
</html>
```